July 4th Postcard to existing clients

5x7 postcard wishing our clients happy 4th of July. Card should read on the back "Thank You For Being A Valued Client!. Stay Safe And Enjoy Your Independence Day Celebrations!"

Patriotic theme with fireworks is ideal. We are a law firm so should still have a feel of professionalism while still being fun since it is for a fun holiday.

```html
<!DOCTYPE html>
<html lang="en">
<head>
<meta charset="utf-8">
<title>Happy 4th of July – Client Postcard</title>
<link rel="stylesheet" href="https://fonts.googleapis.com/css2?family=Cinzel:wght@400&family=Great+Vibes&family=Cormorant+Garamond:wght@500&family=Montserrat:wght@400&family=Lato:wght@400&display=swap">
<style>
  :root {
    --page-bg: #e4e4e4;
    --band-black: #060606;
    --ink-white: #ffffff;
    --ink-dark: #1b1b1b;
    --ink-grey: #6e6e74;
    --flag-blue: #1d2d5c;
    --flag-navy: #0c1430;
    --flag-red: #a8321f;
    --sky-haze: #6f86a8;
    --paper: #ffffff;
    --paper-shade: #bdbdbd;
  }
  html, body {
    margin: 0;
    padding: 0;
    width: 1200px;
    height: 1200px;
    overflow: hidden;
    background: var(--page-bg);
  }
  .canvas {
    position: relative;
    width: 1200px;
    height: 1200px;
  }
  .card {
    position: absolute;
    left: 216px;
    width: 768px;
    overflow: hidden;
    box-shadow: 0 4px 14px rgba(0,0,0,0.25);
  }
  .card-front { top: 50px; height: 552px; background: var(--band-black); }
  .card-back  { top: 622px; height: 550px; }

  .scene-fill {
    position: absolute;
    inset: 0;
    background:
      radial-gradient(ellipse 30% 14% at 17% 82%, rgba(255,190,90,0.95), rgba(233,120,44,0) 70%),
      radial-gradient(ellipse 22% 26% at 28% 26%, rgba(255,200,200,0.55), rgba(255,200,200,0) 70%),
      radial-gradient(ellipse 24% 30% at 62% 40%, rgba(255,150,90,0.6), rgba(255,150,90,0) 70%),
      linear-gradient(160deg, var(--flag-navy) 0%, var(--flag-blue) 28%, var(--sky-haze) 48%, var(--flag-red) 66%, #3a1414 86%, #0a0a0a 100%);
  }
  .card-front .scene-fill { bottom: 128px; }

  .front-title {
    position: absolute;
    left: 0;
    right: 0;
    top: 424px;
    height: 128px;
    margin: 0;
    display: flex;
    justify-content: center;
    align-items: center;
    color: var(--ink-white);
    font-family: "Cinzel", serif;
    font-weight: 400;
    font-size: 62px;
    letter-spacing: 2px;
    line-height: 1;
  }
  .front-title .word { display: block; padding-top: 14px; }
  .front-title .ordinal {
    position: relative;
    display: block;
    width: 84px;
    height: 96px;
    margin: 0 14px 0 12px;
  }
  .front-title .ordinal-num {
    position: absolute;
    left: 0;
    top: -6px;
    font-family: "Montserrat", sans-serif;
    font-size: 104px;
    line-height: 1;
  }
  .front-title .ordinal-suffix {
    position: absolute;
    left: 34px;
    top: 22px;
    font-family: "Great Vibes", cursive;
    font-size: 56px;
    letter-spacing: 0;
  }

  .note-paper {
    position: absolute;
    left: 118px;
    top: 100px;
    width: 500px;
    height: 560px;
    transform: rotate(-7deg);
    transform-origin: top left;
    background:
      radial-gradient(ellipse 70% 60% at 50% 38%, var(--paper) 55%, rgba(255,255,255,0) 100%),
      linear-gradient(180deg, #f4f4f4 0%, var(--paper-shade) 100%);
    box-shadow: 0 6px 18px rgba(0,0,0,0.45);
    text-align: center;
  }
  .note-thanks {
    margin: 58px 20px 0;
    font-family: "Great Vibes", cursive;
    font-size: 52px;
    line-height: 1.05;
    color: var(--ink-dark);
  }
  .note-wish {
    margin: 18px 40px 0;
    font-family: "Cormorant Garamond", serif;
    font-weight: 500;
    font-size: 22px;
    line-height: 1.3;
    color: var(--ink-dark);
  }
  .firm-name {
    margin-top: 70px;
    display: inline-flex;
    align-items: center;
    gap: 12px;
    font-family: "Lato", sans-serif;
    font-size: 34px;
    letter-spacing: 1px;
    color: var(--ink-grey);
  }
  .firm-name .mark {
    width: 18px;
    height: 18px;
    background: var(--ink-grey);
  }
</style>
</head>
<body>
<main class="canvas">
  <section class="card card-front">
    <div class="scene-fill" role="img" aria-label="Photo of a waving American flag over a sunset sky with fireworks bursting behind the Statue of Liberty"></div>
    <h1 class="front-title">
      <span class="word">HAPPY</span>
      <span class="ordinal"><span class="ordinal-num">4</span><span class="ordinal-suffix">th</span></span>
      <span class="word">OF JULY</span>
    </h1>
  </section>

  <section class="card card-back">
    <div class="scene-fill" role="img" aria-label="Photo of a waving American flag over a sunset sky with faint fireworks"></div>
    <div class="note-paper">
      <p class="note-thanks">Thank you for being<br>a valued client!</p>
      <p class="note-wish">Stay Safe And Enjoy Your<br>Independence Day Celebrations!</p>
      <div class="firm-name"><span class="mark"></span>HALVORSEN LAW</div>
    </div>
  </section>
</main>
</body>
</html>
```